Professional Services Business Card Design

We need a business card design for a relatively new (less than one year old) company. Tidewell Advisory Partners, LLC provides professional support services and expert assistance in acquisition management to federal agencies, and also provides acquisition workforce personnel training and development for defense and civilian agencies. The colors used should incorporate the colors found within the company's logo, which is attached.

Font styles to use
Serif
Sans Serif

```html
<!DOCTYPE html>
<html lang="en">
<head>
<meta charset="utf-8">
<title>Tidewell Advisory Partners – Business Card</title>
<link href="https://fonts.googleapis.com/css2?family=Cinzel:wght@400;600&family=Arimo:wght@400&display=swap" rel="stylesheet">
<style>
  :root {
    --backdrop: #3b3b3d;
    --navy: #2f3452;
    --navy-light: #3a3f5e;
    --white: #ffffff;
    --silver: #c6c8d4;
    --muted: #9a9db3;
  }
  * { box-sizing: border-box; margin: 0; padding: 0; }
  html, body { width: 1200px; height: 927px; overflow: hidden; }
  body {
    background: var(--backdrop);
    display: flex;
    flex-direction: column;
    align-items: center;
    justify-content: center;
    gap: 48px;
  }
  .card {
    width: 560px;
    height: 320px;
    background: linear-gradient(135deg, var(--navy-light), var(--navy) 60%);
    border-radius: 4px;
    box-shadow: 0 10px 24px rgba(0,0,0,.35);
    position: relative;
    color: var(--white);
    overflow: hidden;
  }
  /* Front */
  .card-front { display: flex; align-items: center; justify-content: center; }
  .brand { display: flex; align-items: center; gap: 18px; }
  .brand-mark { width: 46px; height: 46px; border: 2px solid var(--white); flex: none; }
  .brand-text { font-family: "Cinzel", serif; text-align: right; }
  .brand-name { font-size: 40px; font-weight: 600; letter-spacing: 3px; line-height: 1; }
  .brand-sub {
    font-size: 19px; letter-spacing: 2px; line-height: 1.2;
    padding-bottom: 6px; border-bottom: 1px solid var(--white);
  }
  .brand-suffix { font-size: 11px; letter-spacing: 3px; margin-top: 5px; }
  /* Back */
  .card-back { padding: 38px 30px 0 300px; }
  .person-name { font-family: "Cinzel", serif; font-weight: 400; font-size: 21px; letter-spacing: 1px; line-height: 1.2; }
  .person-role {
    font-family: "Cinzel", serif; font-size: 10px; letter-spacing: 1.5px; color: var(--silver);
    border-bottom: 1px solid var(--muted); padding-bottom: 6px; margin-bottom: 22px; width: 220px;
  }
  .contact-list { list-style: none; font-family: "Arimo", sans-serif; font-size: 12px; color: var(--silver); }
  .contact-list li { display: flex; align-items: flex-start; gap: 10px; margin-bottom: 9px; line-height: 1.35; }
  .contact-icon { width: 15px; height: 15px; flex: none; margin-top: 1px; }
</style>
</head>
<body>
  <section class="card card-front" aria-label="Card front">
    <div class="brand">
      <span class="brand-mark"></span>
      <div class="brand-text">
        <div class="brand-name">Tidewell</div>
        <div class="brand-sub">Advisory Partners</div>
        <div class="brand-suffix">LLC</div>
      </div>
    </div>
  </section>

  <section class="card card-back" aria-label="Card back">
    <h1 class="person-name">MARCUS ELLERY</h1>
    <p class="person-role">BUSINESS DEVELOPMENT</p>
    <ul class="contact-list">
      <li>
        <svg class="contact-icon" viewBox="0 0 16 16"><circle cx="8" cy="8" r="8" fill="#c6c8d4"/><path d="M8 3.5a2.8 2.8 0 0 0-2.8 2.8C5.2 8.5 8 12 8 12s2.8-3.5 2.8-5.7A2.8 2.8 0 0 0 8 3.5z" fill="#2f3452"/><circle cx="8" cy="6.3" r="1" fill="#c6c8d4"/></svg>
        <span>1420 Harbor Street, Suite 300,<br>Norfolk, VA 23510</span>
      </li>
      <li>
        <svg class="contact-icon" viewBox="0 0 16 16"><circle cx="8" cy="8" r="8" fill="#c6c8d4"/><rect x="5.5" y="3.5" width="5" height="9" rx="1" fill="#2f3452"/></svg>
        <span>757 - 410 28 63</span>
      </li>
      <li>
        <svg class="contact-icon" viewBox="0 0 16 16"><circle cx="8" cy="8" r="8" fill="#c6c8d4"/><path d="M5 4.5l1.6-.4 1 2.2-1 .8a5 5 0 0 0 2.3 2.3l.8-1 2.2 1-.4 1.6C8 11.5 4.5 8 5 4.5z" fill="#2f3452"/></svg>
        <span>757 - 410 28 63</span>
      </li>
      <li>
        <svg class="contact-icon" viewBox="0 0 16 16"><circle cx="8" cy="8" r="8" fill="#c6c8d4"/><rect x="4" y="5" width="8" height="6" fill="none" stroke="#2f3452" stroke-width="1.2"/><path d="M4 5l4 3.5L12 5" fill="none" stroke="#2f3452" stroke-width="1.2"/></svg>
        <span>marcus@tidewelladvisory.com</span>
      </li>
      <li>
        <svg class="contact-icon" viewBox="0 0 16 16"><circle cx="8" cy="8" r="8" fill="#c6c8d4"/><circle cx="8" cy="8" r="4.5" fill="none" stroke="#2f3452" stroke-width="1"/><path d="M3.5 8h9M8 3.5c-2 2.5-2 6.5 0 9M8 3.5c2 2.5 2 6.5 0 9" fill="none" stroke="#2f3452" stroke-width="1"/></svg>
        <span>www.tidewelladvisory.com</span>
      </li>
    </ul>
  </section>
</body>
</html>
```